Online Banner and skyscrapper ads

Design ads for real estate company in Australia to be used on Plot fnder.com.au details below
sizes
Leaderboard Specifications
• Dimensions: 728×90px
• Format: HTML5 or Animated/Static Gif
• Max file size: 100kb (HTML5), 80kb (GIF, JPG, PNG)
• Back-up image: 40kb (GIF, JPG, PNG). Back-up image only required if you supply an HTML5 banner.
• Looping: Yes
• See Leaderboard for more information.
Email Alert Strip Ad (EASA) Specifications
• Dimensions: 472×114 px
• Format: JPEG, PNG or Static GIF
• File Size: 20kb
• Looping: No
Skyscraper Specifications
• Dimensions: 160x600px
• Looping: Yes
• See Skyscraper for more information.
Mega Skyscraper Specifications
• Dimensions: 300x600px
• Format: HTML5 or Animated/Static GIF
• File size: 100kb (Html5) or 80kb (GIF, JPG, PNG)
• Back-up image: 40kb (JPG or PNG). Back-up image only required if you supply an HTML5 banner.
• Looping: Yes
• See Half Page for more information.

I would like them to be quite simple , WYNDALE Your Faulconbridge property experts and another saying WYNDALE your Lawson property experts and WYNDALE your Hazelbrook property experts (3 different versions all up ) and another version MAREE DOLTON your Faulconbridge property expert with logo and her image , i've put a photo of the top banner example and a video of the side banner it has a video in the background that i will get produced if it works

```html
<!DOCTYPE html>
<html lang="en">
<head>
<meta charset="utf-8">
<title>Wyndale – Online Banner Set</title>
<link rel="stylesheet" href="https://fonts.googleapis.com/css2?family=Archivo:wdth,wght@62..125,400..800&family=Roboto:wght@700&display=swap">
<style>
  :root{
    --navy-deep:#08104f;
    --navy:#0c1a6e;
    --navy-mid:#13238a;
    --accent-blue:#2f4ad9;
    --ink-light:#e4e6ea;
    --white:#ffffff;
    --label:#0d1a5c;
    --page:#ffffff;
  }
  *{margin:0;padding:0;box-sizing:border-box}
  html,body{width:1003px;height:1200px;overflow:hidden;background:var(--page)}
  .sheet{position:relative;width:1003px;height:1200px}

  .size-label{
    position:absolute;font-family:"Roboto",Arial,sans-serif;font-weight:700;
    font-size:15px;color:var(--label);letter-spacing:-0.1px;white-space:nowrap;
  }

  .ad{position:absolute;overflow:hidden;color:var(--white)}
  .ad-backdrop{
    position:absolute;inset:0;
    background:linear-gradient(120deg,var(--navy-deep) 0%,var(--navy) 45%,var(--navy-mid) 100%);
  }
  .ad-backdrop.vertical{
    background:linear-gradient(180deg,var(--navy-deep) 0%,var(--navy-deep) 38%,var(--navy) 70%,var(--navy-mid) 100%);
  }

  .wide{
    font-family:"Archivo",Arial,sans-serif;
    font-stretch:125%;
    font-variation-settings:"wdth" 125;
  }

  .brand{
    position:absolute;display:flex;align-items:center;justify-content:center;gap:0.4em;
    font-weight:600;color:var(--ink-light);letter-spacing:0;line-height:1;white-space:nowrap;
  }
  .brand-mark{width:0.55em;height:0.55em;background:var(--ink-light);flex:none}

  .divider{position:absolute;width:1px;background:rgba(228,230,234,0.7)}

  .headline{
    position:absolute;text-align:center;font-weight:600;
    text-transform:uppercase;color:var(--white);letter-spacing:-0.02em;white-space:nowrap;
  }
  .headline .hl{color:var(--accent-blue)}
  .agent-name{
    position:absolute;left:0;right:0;text-align:center;font-weight:700;
    color:var(--accent-blue);letter-spacing:-0.03em;line-height:51px;font-size:54px;
  }

  .portrait{
    position:absolute;
    background:radial-gradient(ellipse at 45% 40%,#c98d76 0%,#a55a4c 35%,#c21d2a 70%,rgba(12,26,110,0) 100%);
    border-radius:48% 48% 0 0;
  }

  /* Leaderboard */
  .leaderboard{left:55px;top:89px;width:893px;height:110px}
  .leaderboard .brand{left:0;width:210px;top:45px;font-size:20px}
  .leaderboard .divider{left:210px;top:24px;height:67px}
  .leaderboard .headline{left:210px;right:213px;top:17px;font-size:29px;line-height:38px}

  /* Email strip */
  .email-strip{left:160px;top:256px;width:680px;height:164px}
  .email-strip .brand{left:0;width:233px;top:70px;font-size:24px}
  .email-strip .divider{left:233px;top:34px;height:96px}
  .email-strip .headline{left:233px;width:304px;top:28px;font-size:27px;line-height:35.5px}

  /* Mega skyscraper */
  .mega{left:221px;top:500px;width:327px;height:653px}
  .mega .brand{left:0;right:0;top:88px;font-size:32px}
  .mega .agent-name{top:163px}
  .mega .headline{left:0;right:0;top:274px;font-size:21px;line-height:29px}
  .mega .portrait{left:24px;top:380px;width:270px;height:273px}

  /* Skyscraper */
  .sky{left:580px;top:500px;width:175px;height:653px}
  .sky .brand{left:0;right:0;top:62px;font-size:17px}
  .sky .headline{left:0;right:0;top:127px;font-size:21px;line-height:28.6px}
</style>
</head>
<body>
<main class="sheet">

  <p class="size-label" style="left:55px;top:50px">LEADERBOARD (TOP BANNER)</p>
  <section class="ad leaderboard">
    <div class="ad-backdrop" role="img" aria-label="Background footage of a modern office building in deep blue tones"></div>
    <div class="brand wide"><span class="brand-mark"></span>WYNDALE</div>
    <div class="divider"></div>
    <h2 class="headline wide">Your <span class="hl">Faulconbridge</span><br>Property Experts</h2>
  </section>

  <p class="size-label" style="left:160px;top:222px">EMAIL ALERT STRIP AD (EASA)</p>
  <section class="ad email-strip">
    <div class="ad-backdrop" role="img" aria-label="Background image of a modern office building in deep blue tones"></div>
    <div class="brand wide"><span class="brand-mark"></span>WYNDALE</div>
    <div class="divider"></div>
    <h2 class="headline wide">Your Lawson<br><span class="hl">Property</span><br>Experts</h2>
  </section>

  <p class="size-label" style="left:221px;top:463px">MEGA SKYSCRAPER (LARGE SIDE BANNER)</p>
  <section class="ad mega">
    <div class="ad-backdrop vertical" role="img" aria-label="Background footage of a modern office building in deep blue tones"></div>
    <div class="brand wide"><span class="brand-mark"></span>WYNDALE</div>
    <h2 class="agent-name wide">MAREE<br>DOLTON</h2>
    <p class="headline wide">Your<br>Faulconbridge<br>Property Expert</p>
    <div class="portrait" role="img" aria-label="Portrait photo of agent Maree Dolton smiling, wearing a red jacket"></div>
  </section>

  <p class="size-label" style="left:580px;top:463px">SKYSCRAPER (SIDE BANNER)</p>
  <section class="ad sky">
    <div class="ad-backdrop vertical" role="img" aria-label="Background footage of a modern office building in deep blue tones"></div>
    <div class="brand wide"><span class="brand-mark"></span>WYNDALE</div>
    <h2 class="headline wide">Your<br>Hazel<br>Brook<br><span class="hl">Property</span><br>Experts</h2>
  </section>

</main>
</body>
</html>
```